Medical Learning Web Design Project

The web site will be a site for medical students. It is aimed at providing a collaborative place for students to study, learn, question each other and challenge each other with learning. The site needs to have a section on the page that is for the content and this needs to be relatively clean and clinical. The surrounding elements will be informative (for the statistics, challenge etc). There will also be a slide-out screen that allows for the social/friend elements of the site.

The colour scheme needs to be clean and clinical where appropriate, but also engaging and exciting for the social/competitive elements.
Updates

Just for clarity: The site isn't expected to be 'coded' ... it is just the layered PSD files that I need.

Also, with regards to the navigation buttons ... they will never ALL be present at the same time so don't feel the need to design all on one page, but creativity around allowing few or many on a page will be an advantage ...

Thanks

Hi,

Please note that the image uploaded has been done as a wireframe by the developers. I am looking for a more creative and engaging way of presenting that content ...

Thanks

Hi all

Thank you all for the designs so far ...!

Please have a look at the new uploaded file, I am also looking not just for a 'templated home page' but also some different layouts that are represented in these wireframes. If the various layouts represented can be condensed down into 1 or 2 page templates with appropriate colour schemes to capture the type of content on the page (as already mentioned ... social .. competitive ... learning), then that will help me live the concepts better too! The friends tab for instance I have envisaged as a slider covering the screen and then sliding back when complete ... but let me see what creativity you can give to this ...!

Many thanks

Reason: Just allowing for final tweaks ...

Target Market(s)

Medical Students

Industry/Entity Type

Medical

Requirements
Must have
• - Not cluttered appearance
- Dynamic navigation (ie. site will be developed to only show relevant navigation buttons on each page ...)
- Navigation buttons (need to be individual buttons) will be: 'Home', 'Take the tour', 'What your peers say', 'Subscriptions', 'Free Signup', 'Contact us', 'Moderation', 'Statistics', 'Competition', 'Answer Questions', 'Post Questions', 'My profile', 'Friends'
- Please also ensure it is engaging for social elements and competitive elements (perhaps slightly different design for pages focussed on each element)
- Please also ensure that there is a masculine design and feminine design that has continuity for the site but depending on gender the design can be tailored to be more appealing (that means perhaps male social design, male competitive design, female social design, female competitive design ... without loosing continuity through the site).
- Photoshop PSD format
- Pixel perfect at least 1000 pixels wide (but the design needs to allow for various monitor sizes (only desktop or laptops ... not tablets or smart phones)

```html
<!DOCTYPE html>
<html lang="en">
<head>
<meta charset="utf-8">
<title>Vitaro – The Medical Peer Review</title>
<link rel="stylesheet" href="https://fonts.googleapis.com/css2?family=Source+Sans+3:ital,wght@0,400;0,600;0,700;1,400;1,600&display=swap">
<style>
:root{
  --green:#6aaa3a;
  --green-dark:#4e9a2e;
  --green-light:#8cc152;
  --ink:#222;
  --ink-soft:#444;
  --muted:#777;
  --line:#cfcfcf;
  --panel:#f4f4f4;
  --dark:#262626;
  --white:#fff;
}
*{box-sizing:border-box;margin:0;padding:0}
html,body{width:1096px;height:1200px;overflow:hidden;background:var(--white)}
body{font-family:"Source Sans 3",Arial,sans-serif;color:var(--ink)}
.page{position:relative;width:1024px;height:1121px;transform:scale(1.0703);transform-origin:0 0}
.abs{position:absolute}
.top-rule{left:0;top:0;width:1024px;height:4px;background:var(--green)}

/* header */
.brand{left:25px;top:33px;display:flex;align-items:center;gap:12px}
.brand-mark{width:34px;height:34px;background:var(--green);border-radius:3px}
.brand-name{font-size:38px;font-weight:400;color:#1d1d1d;line-height:1;letter-spacing:.5px}
.brand-tag{left:57px;top:76px;font-size:14px;color:var(--ink-soft)}
.quote{left:220px;top:52px;width:382px;text-align:right;font-size:12px;font-style:italic;line-height:15px;color:var(--ink)}
.stats-call{left:300px;top:94px;width:268px;text-align:center;font-size:13.5px;font-style:italic;font-weight:700;color:var(--green-dark)}
.web-label{left:699px;top:14px;font-size:13px;color:var(--ink)}
.web-icons{left:820px;top:13px;display:flex;gap:3px}
.web-icons span{width:19px;height:19px;border-radius:3px;background:#5b7bb5}
.web-icons span:nth-child(2){background:#5bb8e6}
.web-icons span:nth-child(3){background:#2a72b0}
.web-icons span:nth-child(4){background:#3b5c91}
.web-icons span:nth-child(5){background:#c9c9c9}
.web-icons span:nth-child(6){background:#3aa43a}
.web-icons span:nth-child(7){background:#e07b27}
.web-icons span:nth-child(8){background:#57b53a}
.login label{position:absolute;font-size:13.5px;color:var(--ink)}
.field{position:absolute;height:23px;border:1px solid #bdbdbd;background:var(--white)}
.login small{position:absolute;font-size:10.5px;color:var(--muted)}
.login .forgot{text-decoration:underline}
.login-btn{position:absolute;left:936px;top:71px;width:60px;height:27px;border-radius:4px;background:linear-gradient(#3a3a3a,#111);color:var(--white);font-size:13px;text-align:center;line-height:27px}

/* navigation */
.nav{left:189px;top:143px;height:44px;display:flex;border:1px solid var(--line);border-bottom:none;background:var(--white)}
.nav a{display:block;height:43px;line-height:43px;text-align:center;font-size:15px;color:var(--ink);text-decoration:none;border-left:1px solid var(--line)}
.nav a:first-child{border-left:none}
.nav a.current{background:linear-gradient(#8cc152,#5ea23a);color:var(--white)}
.nav-band{left:0;top:186px;width:1024px;height:8px;background:var(--green)}

/* notice */
.notice{left:21px;top:206px;width:981px;height:35px;border:1px solid var(--line);border-radius:4px}
.notice p{position:absolute;left:17px;top:8px;font-size:13px;color:#555}
.notice b{font-weight:400;color:var(--ink)}
.share{position:absolute;top:7px;display:flex;align-items:center;gap:3px;font-size:11px}
.share .btn{height:18px;padding:0 6px;border:1px solid #b8c6dd;border-radius:2px;background:#eef2f8;line-height:16px;color:#3b5998;display:flex;align-items:center;gap:4px}
.share .btn i{width:10px;height:10px;background:#8aa0c8;display:inline-block}
.share .count{height:18px;padding:0 4px;border:1px solid #bbb;background:var(--white);line-height:16px;color:#333}

/* hero */
.hero{left:24px;top:255px;width:978px;height:404px;border:1px solid #c9c9c9;border-radius:8px;background:linear-gradient(#ececec,#fafafa 40%,#f6f6f6);box-shadow:0 3px 4px rgba(0,0,0,.06)}
.hero-title{left:72px;top:291px;font-size:26px;color:#1d1d1d}
.hero-title span{font-size:21px}
.features{left:75px;top:340px;width:333px;list-style:none}
.features li{height:34.7px;display:flex;align-items:center;gap:10px;font-size:14.5px;font-weight:600;color:#333;border-bottom:1px solid #dcdcdc}
.features li:last-child{border-bottom:none}
.features svg{flex:none}
.tile{position:absolute;width:228px;height:154px;background:var(--white);border:1px solid #ddd;padding:6px;box-shadow:0 1px 3px rgba(0,0,0,.12)}
.tile > div{width:100%;height:100%}
.fill-instruments{background:linear-gradient(135deg,#f1f1f1,#bfc6cc 55%,#7b8389)}
.fill-infographic{background:linear-gradient(160deg,#8cbf48,#6aa532 50%,#e9f0d8)}
.fill-team{background:linear-gradient(120deg,#c9dff2,#eef4fa 45%,#a8b7c2)}
.chart{background:#f3f3f3}
.dots{left:476px;top:634px;display:flex;gap:4px}
.dots span{width:11px;height:11px;border-radius:50%;background:#c8c8c8}
.dots span:first-child{background:var(--green)}

/* lower panels */
.panel{position:absolute;top:684px;height:295px;border:1px solid #c9c9c9;border-radius:4px;background:var(--white)}
.video-panel{left:25px;width:401px}
.video-panel h2{position:absolute;left:21px;top:16px;font-size:18.5px;font-weight:400}
.player{position:absolute;left:15px;top:49px;width:374px;height:236px;background:#000}
.player-bar{position:absolute;left:0;bottom:0;width:100%;height:30px;background:#2c2c2c;border-top:1px solid #444}
.feed-panel{left:435px;width:277px;border-radius:0;border-color:#999}
.feed-head{position:absolute;left:0;top:0;width:100%;height:52px;background:var(--dark);color:var(--white);padding:10px 0 0 51px}
.feed-head small{display:block;font-size:11.5px;color:#ddd}
.feed-head strong{font-size:17px;font-weight:400}
.post{position:absolute;left:14px;width:250px;font-size:12px;line-height:17px;color:#333}
.post time{display:block;margin-top:4px;color:var(--green-dark)}
.post-rule{position:absolute;left:0;width:100%;height:1px;background:#ddd}
.feed-foot{position:absolute;left:0;bottom:0;width:100%;height:26px;background:var(--dark);font-size:12px;color:var(--white);line-height:26px;padding:0 14px 0 11px;display:flex;justify-content:space-between}
.feed-foot b{font-weight:400;color:#7ec4e8}
.fans-panel{left:725px;width:277px;border-radius:0;border-color:#999}
.fans-avatar{position:absolute;left:12px;top:11px;width:69px;height:58px;background:#eee}
.fans-title{position:absolute;left:94px;top:11px;font-size:15px}
.fans-title span{font-size:12px}
.like-btn{position:absolute;left:95px;top:37px;height:18px;padding:0 6px;border:1px solid #b8c6dd;background:#eef2f8;font-size:12px;line-height:16px;color:#3b5998}
.you-like{position:absolute;left:154px;top:38px;font-size:12px}
.fans-rule{position:absolute;left:6px;width:265px;height:1px;background:#ddd}
.fans-count{position:absolute;left:13px;top:88px;font-size:12px}
.faces{position:absolute;left:12px;top:113px;width:260px;display:grid;grid-template-columns:repeat(5,47px);column-gap:4.5px;row-gap:10px}
.faces figure{width:47px;font-size:11px;color:#555;text-align:center}
.faces figure div{width:47px;height:47px;background:linear-gradient(#d9c2a8,#8f7462);border:1px solid #bbb;margin-bottom:2px}
.plugin-note{position:absolute;left:36px;top:270px;font-size:11.5px;color:#444}

/* footer */
.footer{left:0;top:1022px;width:1024px;height:99px;background:linear-gradient(#7fb428,#5ea13c)}
.footer-links{position:absolute;top:16px;width:100%;text-align:center;font-size:12.5px;font-weight:700;color:var(--white)}
.footer-links a{color:var(--white);text-decoration:none}
.footer-links i{font-style:normal;margin:0 12px}
.footer-note{position:absolute;width:100%;text-align:center;font-size:12px;font-weight:600;color:#dcedc6}
</style>
</head>
<body>
<div class="page">
  <div class="abs top-rule"></div>

  <header>
    <div class="abs brand"><span class="brand-mark"></span><span class="brand-name">Vitaro</span></div>
    <div class="abs brand-tag">The Medical Peer Review</div>
    <p class="abs quote">Lorem ipsum dolor sit ametadipiscing elit. Nam cursus. Morbi ut mi. Nullam<br>---Tom, doctor in training, Northbridge University</p>
    <p class="abs stats-call">How will your stats company?</p>

    <div class="abs web-label">Vitaro on the web:</div>
    <div class="abs web-icons" aria-label="Social links"><span></span><span></span><span></span><span></span><span></span><span></span><span></span><span></span></div>

    <form class="login">
      <label style="left:659px;top:54px">Username</label>
      <span class="field" style="left:659px;top:74px;width:131px"></span>
      <small style="left:684px;top:98px">Keep Me Signed In</small>
      <label style="left:800px;top:54px">Password</label>
      <span class="field" style="left:800px;top:74px;width:131px"></span>
      <small class="forgot" style="left:801px;top:99px">Forgot password</small>
      <span class="login-btn">Login</span>
    </form>
  </header>

  <nav class="abs nav">
    <a class="current" style="width:101px">Home</a>
    <a style="width:123px">Take The Tour</a>
    <a style="width:173px">What Your Peers Say</a>
    <a style="width:160px">Subscription Plans</a>
    <a style="width:119px">Free Signup</a>
    <a style="width:137px">Contact Us</a>
  </nav>
  <div class="abs nav-band"></div>

  <div class="abs notice">
    <p><b>About 2 days ago:</b> Vitaro is now on Circlebook. Follow us here.</p>
    <div class="share" style="left:686px"><span class="btn"><i></i>Like</span><span class="count">84</span></div>
    <div class="share" style="left:789px"><span class="btn" style="color:#555;border-color:#bbb;background:#f5f5f5">+1</span><span class="count">2</span></div>
    <div class="share" style="left:862px"><span class="btn" style="color:#2a7ab0;border-color:#9cc8e4;background:#e8f4fb"><i style="background:#6ab8e4"></i>Post</span><span class="count" style="padding:0 12px">11</span></div>
  </div>

  <section class="abs hero">
  </section>
  <h1 class="abs hero-title" style="font-weight:400">Vitaro <span>- The Medical Peer Review</span></h1>
  <ul class="abs features">
    <li><svg width="14" height="12" viewBox="0 0 14 12"><path d="M1 6l4 4 8-9" fill="none" stroke="#4e9a2e" stroke-width="2.6"/></svg>Test yoru Medical Knowledge</li>
    <li><svg width="14" height="12" viewBox="0 0 14 12"><path d="M1 6l4 4 8-9" fill="none" stroke="#4e9a2e" stroke-width="2.6"/></svg>Answer a vast array of medical questions</li>
    <li><svg width="14" height="12" viewBox="0 0 14 12"><path d="M1 6l4 4 8-9" fill="none" stroke="#4e9a2e" stroke-width="2.6"/></svg>Earn trophies as your knowledge increases</li>
    <li><svg width="14" height="12" viewBox="0 0 14 12"><path d="M1 6l4 4 8-9" fill="none" stroke="#4e9a2e" stroke-width="2.6"/></svg>Reate Question from peers</li>
    <li><svg width="14" height="12" viewBox="0 0 14 12"><path d="M1 6l4 4 8-9" fill="none" stroke="#4e9a2e" stroke-width="2.6"/></svg>Ask your own questions</li>
    <li><svg width="14" height="12" viewBox="0 0 14 12"><path d="M1 6l4 4 8-9" fill="none" stroke="#4e9a2e" stroke-width="2.6"/></svg>Link to your friends and check their progress</li>
    <li><svg width="14" height="12" viewBox="0 0 14 12"><path d="M1 6l4 4 8-9" fill="none" stroke="#4e9a2e" stroke-width="2.6"/></svg>29.903 Questions answered!</li>
  </ul>

  <div class="tile" style="left:467px;top:283px"><div class="fill-instruments" role="img" aria-label="Photo of a stethoscope and pen on a medical chart"></div></div>
  <div class="tile" style="left:724px;top:283px"><div class="fill-infographic" role="img" aria-label="Green infographic about records management timings"></div></div>
  <div class="tile" style="left:467px;top:455px;height:153px">
    <svg class="chart" width="214" height="139" viewBox="0 0 214 139" role="img" aria-label="Bar chart of top countries by medical graduates">
      <rect width="214" height="139" fill="#f3f3f3"/>
      <path d="M18 20V132H208" stroke="#999" fill="none"/>
      <g fill="#3b7bd9">
        <rect x="26" y="44" width="8" height="88"/><rect x="45" y="50" width="8" height="82"/>
        <rect x="63" y="57" width="8" height="75"/><rect x="82" y="68" width="8" height="64"/>
        <rect x="100" y="78" width="8" height="54"/><rect x="118" y="78" width="8" height="54"/>
        <rect x="137" y="80" width="8" height="52"/><rect x="156" y="86" width="8" height="46"/>
        <rect x="174" y="87" width="8" height="45"/><rect x="193" y="93" width="8" height="39"/>
      </g>
    </svg>
  </div>
  <div class="tile" style="left:724px;top:455px;height:153px"><div class="fill-team" role="img" aria-label="Photo of a smiling team of doctors in white coats"></div></div>
  <div class="abs dots"><span></span><span></span><span></span><span></span><span></span></div>

  <section class="panel video-panel">
    <h2>How Vitaro Works</h2>
    <div class="player">
      <svg class="abs" style="left:171px;top:92px" width="32" height="40" viewBox="0 0 32 40"><path d="M0 0L32 20L0 40Z" fill="#fff"/></svg>
      <div class="player-bar">
        <svg class="abs" style="left:12px;top:9px" width="10" height="12" viewBox="0 0 10 12"><path d="M0 0L10 6L0 12Z" fill="#fff"/></svg>
        <span class="abs" style="left:31px;top:0;width:1px;height:30px;background:#444"></span>
        <span class="abs" style="left:40px;top:14px;width:266px;height:2px;background:#666"></span>
        <span class="abs" style="left:52px;top:10px;width:10px;height:10px;border-radius:50%;background:#fff"></span>
        <span class="abs" style="left:313px;top:0;width:1px;height:30px;background:#444"></span>
        <span class="abs" style="left:320px;top:9px;width:14px;height:13px;border-radius:3px;background:#555"></span>
        <span class="abs" style="left:341px;top:9px;width:21px;height:13px;border-radius:6px;background:#555"></span>
      </div>
    </div>
  </section>

  <section class="panel feed-panel">
    <div class="feed-head"><small>Vitaro Medical Peer Review</small><strong>Vitaro</strong></div>
    <p class="post" style="top:65px">Lorem ipsum dolor sit amet, consectetuer adipiscing elit. Nam cursus. Morbi ut mi. Nullam<time>Posted on 10.11.2012</time></p>
    <div class="post-rule" style="top:127px"></div>
    <p class="post" style="top:132px">Lorem ipsum dolor sit amet, consectetuer adipiscing elit. Nam cursus. Morbi ut mi. Nullam<time>Posted on 10.11.2012</time></p>
    <div class="post-rule" style="top:192px"></div>
    <p class="post" style="top:199px">Lorem ipsum dolor sit amet, consectetuer adipiscing elit. Nam cursus. Morbi ut mi. Nullam<time>Posted on 10.11.2012</time></p>
    <div class="feed-foot"><b>Chirper</b><span>Join the Conversation</span></div>
  </section>

  <section class="panel fans-panel">
    <div class="fans-avatar"></div>
    <div class="fans-title">Vitaro <span>on circlebook</span></div>
    <span class="like-btn">Like</span>
    <span class="you-like">You like this.</span>
    <div class="fans-rule" style="top:80px"></div>
    <div class="fans-count">22407 people ike Vitaro</div>
    <div class="faces">
      <figure><div role="img" aria-label="Member portrait"></div>Name</figure>
      <figure><div role="img" aria-label="Member portrait"></div>Name</figure>
      <figure><div role="img" aria-label="Member portrait"></div>Name</figure>
      <figure><div role="img" aria-label="Member portrait"></div>Name</figure>
      <figure><div role="img" aria-label="Member portrait"></div>Name</figure>
      <figure><div role="img" aria-label="Member portrait"></div>Name</figure>
      <figure><div role="img" aria-label="Member portrait"></div>Name</figure>
      <figure><div role="img" aria-label="Member portrait"></div>Name</figure>
      <figure><div role="img" aria-label="Member portrait"></div>Name</figure>
      <figure><div role="img" aria-label="Member portrait"></div>Name</figure>
    </div>
    <div class="fans-rule" style="top:262px"></div>
    <div class="plugin-note">Circlebook social plugin</div>
  </section>

  <footer class="abs footer">
    <div class="footer-links"><a>Home</a><i>|</i><a>Take The Tour</a><i>|</i><a>What Your Peers Say</a><i>|</i><a>Subscription Plans</a><i>|</i><a>Free Signup</a><i>|</i><a>Contact Us</a><i>|</i><a>Sitemap</a></div>
    <div class="footer-note" style="top:47px">© Copyright 2012 Vitaro Limited</div>
    <div class="footer-note" style="top:65px">powred by Fennlow</div>
  </footer>
</div>
</body>
</html>
```